IT-Dienstleister sucht modernes Visitenkarten und Briefpapier Design
Sehr gute Zusammenarbeit und Designs. Kann ich jedem weiterempfehlen. TOP!!!
Zielgruppe
Wir bieten maßgeschneiderte Softwareentwicklungsleistungen für Unternehmen jeder Größe und Branche.
Aufgabenstellung
Das Design sollte eigentlich ziemlich schlicht, aber trotzdem modern sein und zu dem bestehenden Firmen-Logo passen. Desweiteren sollte es natürlich auch zum dem Thema Softwareentwicklung passen.

```html
<!DOCTYPE html>
<html lang="de">
<head>
<meta charset="utf-8">
<title>nodexa – Briefpapier</title>
<link href="https://fonts.googleapis.com/css2?family=Jura:wght@400;500;600;700&display=swap" rel="stylesheet">
<style>
  :root {
    --backdrop: #b7b9bb;
    --paper: #ffffff;
    --teal-dark: #4a8d96;
    --teal-light: #6cc5cf;
    --teal-icon: #5ab8c4;
    --text-grey: #6d6e70;
    --text-dark: #5a5b5d;
    --fold-mark: #9cc9cf;
  }
  * { margin: 0; padding: 0; box-sizing: border-box; }
  html, body { width: 900px; height: 1200px; overflow: hidden; background: var(--backdrop); }
  body { position: relative; font-family: "Jura", sans-serif; color: var(--text-grey); }

  .letterhead {
    position: absolute; left: 50px; top: 34px;
    width: 800px; height: 1131px; background: var(--paper);
  }
  .band {
    position: absolute; left: 95px; right: 0; height: 11px;
    background: linear-gradient(90deg, var(--teal-dark), var(--teal-light));
  }
  .band--top { top: 0; }
  .band--bottom { top: 1120px; }

  .brand {
    position: absolute; right: 58px; top: 62px; width: 260px; text-align: center;
  }
  .brand__name {
    display: flex; align-items: center; justify-content: center; gap: 12px;
    font-size: 64px; font-weight: 500; line-height: 1; color: var(--text-grey);
  }
  .brand__dot { width: 26px; height: 26px; border-radius: 50%; background: var(--teal-icon); }
  .brand__tagline {
    margin-top: 26px; font-size: 17px; font-weight: 600; letter-spacing: 0.3px; color: var(--text-grey);
  }

  .sender-line {
    position: absolute; left: 95px; top: 185px; font-size: 9.6px; letter-spacing: 0.2px;
  }
  .sender-line strong { font-weight: 700; color: var(--text-dark); }
  .sender-line .sep { color: var(--teal-icon); margin: 0 3px; }

  .contact {
    position: absolute; left: 603px; top: 185px; font-size: 10px; line-height: 16px; letter-spacing: 0.2px;
  }
  .contact__row { display: flex; align-items: flex-start; }
  .contact__row + .contact__row { margin-top: 4px; }
  .contact__row--tight { margin-top: 0 !important; }
  .contact__icon { width: 12px; height: 12px; margin: 2px 10px 0 0; flex: none; fill: var(--teal-icon); }
  .contact strong { font-weight: 700; color: var(--text-dark); }

  .fold-mark {
    position: absolute; left: 0; width: 19px; height: 1px; background: var(--fold-mark);
  }

  .legal {
    position: absolute; top: 1063px; font-size: 9.6px; line-height: 16px; letter-spacing: 0.2px;
  }
  .legal--management { left: 95px; }
  .legal--register { left: 396px; }
  .legal--bank { left: 627px; }
</style>
</head>
<body>
  <main class="letterhead">
    <div class="band band--top"></div>

    <header class="brand">
      <div class="brand__name"><span class="brand__dot"></span>nodexa</div>
      <div class="brand__tagline">SOFTWARE DEVELOPMENT</div>
    </header>

    <p class="sender-line"><strong>nodexa GmbH</strong><span class="sep">|</span>Lindenweg 14<span class="sep">|</span>54329 Kaltenbrunn</p>

    <address class="contact" style="font-style:normal">
      <div class="contact__row">
        <svg class="contact__icon" viewBox="0 0 12 12"><path d="M6 0a4 4 0 0 0-4 4c0 3 4 8 4 8s4-5 4-8a4 4 0 0 0-4-4zm0 5.6A1.6 1.6 0 1 1 6 2.4a1.6 1.6 0 0 1 0 3.2z"/></svg>
        <div><strong>nodexa GmbH</strong><br>Lindenweg 14<br>54329 Kaltenbrunn</div>
      </div>
      <div class="contact__row">
        <svg class="contact__icon" viewBox="0 0 12 12"><path d="M3 1l2 2.2-1.2 1.4c.6 1.4 1.8 2.6 3.2 3.2L8.4 6.6 11 8.6 9.8 11C5 11 1 7 1 2.2z"/></svg>
        <div>+49 (0) 555 28140713</div>
      </div>
      <div class="contact__row contact__row--tight">
        <svg class="contact__icon" viewBox="0 0 12 12"><path d="M3 1h6v3H3zM1 5h10v4H9v2H3V9H1zm3 2v3h4V7z"/></svg>
        <div>+49 (0) 555 28140716</div>
      </div>
      <div class="contact__row">
        <svg class="contact__icon" viewBox="0 0 12 12"><circle cx="6" cy="6" r="5" fill="none" stroke="var(--teal-icon)" stroke-width="1.4"/><path d="M1 6h10M6 1c-2.5 3-2.5 7 0 10M6 1c2.5 3 2.5 7 0 10" fill="none" stroke="var(--teal-icon)" stroke-width="1"/></svg>
        <div>www.nodexa.de</div>
      </div>
      <div class="contact__row contact__row--tight">
        <svg class="contact__icon" viewBox="0 0 12 12"><path d="M1 2.5h10v7H1z"/><path d="M1 2.5l5 4 5-4" fill="none" stroke="#fff" stroke-width="1"/></svg>
        <div>info@nodexa.de</div>
      </div>
    </address>

    <div class="fold-mark" style="top:400px"></div>
    <div class="fold-mark" style="top:566px"></div>
    <div class="fold-mark" style="top:799px"></div>

    <footer>
      <div class="legal legal--management">Geschäftsführer: Tobias Reimann<br>Registergericht: Amtsgericht Kaltenbrunn</div>
      <div class="legal legal--register">Registernummer: HRB 40218<br>USt-IdNr.: DE123456789</div>
      <div class="legal legal--bank">Bankverbindung: Musterbank<br>IBAN: 1234 5678 910 1112 30<br>BIC: XXXXXXXXXX</div>
    </footer>

    <div class="band band--bottom"></div>
  </main>
</body>
</html>
```